Private Chef booking platform landing page design

I need an amazing design for a landing page for my upcoming private chef booking platform Dinvora. You can view my current page here: www.dinvora.co.uk/mainindex.php. The design on this page is wrong right now. This platform is in Beta and the main purpose is to sign up chefs. Similar to what Ridelix.com is doing with their website -> become a driver. In my case we should have a button that says "become a chef", state the benefits of becoming a chef such as earning extra money, managing your time and bookings, increasing your client base and be creative with your food menus at the same time. Also, somewhere on the website it needs to say that we are currently in Beta mode and sign up to help us grow. In terms of visuals, I want the design to be sleek and clean and also adaptable to mobile devices as I am using html5. You can also re-design the current logo and choose any colours you think would be suitable for such a concept. Similar concept websites: platewander.com and cookvey.com
Updates

Target Market(s)

upper middle class

Industry/Entity Type

Chef

Number of Pages Required

1 page

Font styles to use
Sans Serif

Requirements
Must have
• see brief and check platewander.com and cookvey.com for inspiration and also ridelix.com
Nice to have
• see brief
Should not have
• bad visuals

```html
<!DOCTYPE html>
<html lang="en">
<head>
<meta charset="utf-8">
<title>Dinvora — Chefs made meals in your home</title>
<link rel="stylesheet" href="https://fonts.googleapis.com/css2?family=Lato:ital,wght@0,400;0,700;0,900;1,400&family=Oswald:wght@400&family=Kaushan+Script&family=Great+Vibes&family=Alfa+Slab+One&display=swap">
<style>
  :root {
    --orange: #e0500e;
    --orange-deep: #d94f0c;
    --orange-mid: #f26522;
    --orange-soft: #f47c3c;
    --orange-pale: #f89a66;
    --ink: #111111;
    --charcoal: #3a3a3a;
    --footer: #333333;
    --paper: #ffffff;
    --quote-bg: #ebebea;
    --body-text: #6b6b6b;
    --muted: #8a8a8a;
  }
  * { box-sizing: border-box; margin: 0; padding: 0; }
  html, body { width: 973px; height: 1200px; overflow: hidden; background: var(--paper); }
  body { position: relative; font-family: "Lato", Arial, sans-serif; color: var(--ink); }

  /* Header */
  .site-header { position: absolute; top: 0; left: 0; width: 973px; height: 50px; background: var(--paper); z-index: 3; box-shadow: 0 2px 4px rgba(0,0,0,.08); }
  .menu-toggle { position: absolute; left: 60px; top: 17px; width: 21px; }
  .menu-toggle span { display: block; height: 2px; background: #9a9a9a; margin-bottom: 5px; }
  .auth-links { position: absolute; right: 60px; top: 13px; display: flex; gap: 8px; }
  .auth-links a { display: block; width: 82px; height: 27px; border: 2px solid var(--ink); border-radius: 3px; font-size: 12px; line-height: 23px; text-align: center; text-decoration: none; color: var(--ink); }
  .auth-links a.login { border-color: var(--orange); color: var(--orange); }

  .brand-badge { position: absolute; left: 415px; top: 0; width: 171px; height: 100px; background: var(--paper); border-radius: 0 0 80px 80px; z-index: 4; display: flex; align-items: center; justify-content: center; box-shadow: 0 3px 6px rgba(0,0,0,.1); }
  .brand-name { font-family: "Lato", Arial, sans-serif; font-weight: 700; font-size: 30px; color: var(--ink); margin-top: 14px; }

  /* Hero */
  .hero { position: absolute; top: 50px; left: 0; width: 973px; height: 517px; background: linear-gradient(90deg, #ece7e2 0%, #e7ddd3 18%, #efe9e4 38%, #f4f2f0 55%, #dfe5ea 75%, #eef1f3 100%); }
  .hero-photo { position: absolute; left: 60px; top: 0; width: 590px; height: 517px; background: radial-gradient(ellipse at 40% 35%, #e2b89a 0%, #efe6df 35%, rgba(245,243,241,0) 70%); }
  .hero-title { position: absolute; left: 545px; top: 186px; font-family: "Oswald", "Arial Narrow", sans-serif; font-size: 56px; line-height: 1; color: var(--ink); letter-spacing: -0.5px; }
  .hero-subtitle { position: absolute; left: 632px; top: 244px; font-family: "Kaushan Script", cursive; font-size: 48px; color: var(--ink); }
  .hero-actions { position: absolute; left: 493px; top: 338px; display: flex; gap: 9px; }
  .hero-actions a { display: flex; align-items: center; justify-content: center; width: 205px; height: 63px; font-family: "Alfa Slab One", Georgia, serif; font-size: 17px; line-height: 21px; color: #fff; text-align: center; text-decoration: none; border-radius: 2px; border-bottom: 3px solid rgba(0,0,0,.25); }
  .btn-become { background: var(--orange); }
  .btn-how { background: var(--charcoal); }
  .btn-create { position: absolute; left: 227px; top: 528px; width: 228px; height: 39px; background: var(--ink); color: #fff; font-weight: 700; font-size: 15px; line-height: 39px; text-align: center; text-decoration: none; border-radius: 3px 3px 0 0; z-index: 2; }

  /* Welcome */
  .welcome-mark { position: absolute; left: 60px; top: 608px; width: 150px; }
  .welcome-mark .lead { display: block; text-align: right; font-family: "Great Vibes", cursive; font-size: 20px; color: var(--ink); }
  .welcome-mark .name { display: block; font-family: "Lato", Arial, sans-serif; font-weight: 700; font-size: 32px; color: var(--ink); margin-top: -2px; }
  .welcome-copy { position: absolute; left: 243px; top: 608px; width: 380px; font-size: 12.2px; line-height: 21px; color: var(--body-text); }

  /* Testimonial */
  .testimonial { position: absolute; left: 60px; top: 850px; width: 561px; height: 155px; background: var(--quote-bg); border-radius: 2px; }
  .quote-mark { position: absolute; left: 265px; top: -30px; font-family: Georgia, serif; font-weight: 700; font-size: 72px; color: #f1f1f1; line-height: 1; }
  .testimonial blockquote { position: absolute; left: 51px; top: 33px; width: 465px; font-style: italic; font-size: 11.5px; line-height: 19.5px; color: #666; }
  .author-photo { position: absolute; left: 374px; top: 985px; width: 66px; height: 66px; border-radius: 50%; background: radial-gradient(circle at 50% 45%, #d8a98a, #8a6450); border: 3px solid #fff; box-shadow: 0 1px 3px rgba(0,0,0,.2); }
  .author { position: absolute; left: 448px; top: 1008px; }
  .author-name { font-family: "Great Vibes", cursive; font-size: 20px; color: var(--orange); }
  .author-name::before { content: ""; display: inline-block; width: 18px; height: 2px; background: var(--orange); vertical-align: middle; margin-right: 6px; }
  .author-role { font-size: 10.5px; color: #666; margin-left: 25px; margin-top: -2px; }

  /* Benefits */
  .benefits { position: absolute; left: 680px; top: 567px; width: 233px; height: 510px; }
  .benefits > svg { position: absolute; left: 0; top: 0; }
  .benefits-badge { position: absolute; left: 751px; top: 523px; width: 94px; height: 88px; border-radius: 50%; background: var(--orange); }
  .benefits-title { position: absolute; left: 680px; top: 620px; width: 233px; text-align: center; color: #fff; font-weight: 700; font-size: 19px; }
  .benefit { position: absolute; left: 643px; width: 270px; height: 74px; display: flex; align-items: center; }
  .benefit-icon { width: 74px; height: 74px; border-radius: 50%; background: var(--ink); border: 3px solid #fff; display: flex; align-items: center; justify-content: center; flex: none; }
  .benefit-label { margin-left: 14px; color: #fff; font-weight: 700; font-size: 14.5px; line-height: 16px; }

  /* Footer */
  .site-footer { position: absolute; left: 0; top: 1110px; width: 973px; height: 90px; background: var(--footer); color: #fff; }
  .social { position: absolute; top: 26px; left: 0; width: 973px; display: flex; justify-content: center; gap: 14px; font-size: 11px; }
  .social span { display: flex; align-items: center; }
  .social span::before { content: ""; width: 11px; height: 11px; background: #fff; margin-right: 5px; border-radius: 1px; }
  .copyright { position: absolute; top: 59px; width: 973px; text-align: center; font-size: 10.5px; }
</style>
</head>
<body>

<header class="site-header">
  <div class="menu-toggle" aria-label="Menu"><span></span><span></span><span></span></div>
  <nav class="auth-links">
    <a href="#" class="signup">SIGN UP</a>
    <a href="#" class="login">LOGIN</a>
  </nav>
</header>
<div class="brand-badge"><span class="brand-name">Dinvora</span></div>

<section class="hero">
  <div class="hero-photo" role="img" aria-label="Smiling chef in white jacket and toque with arms crossed in a bright kitchen"></div>
  <h1 class="hero-title">Chefs made meals</h1>
  <p class="hero-subtitle">in your home</p>
  <div class="hero-actions">
    <a href="#" class="btn-become">BECOME A<br>PRIVATE CHEF</a>
    <a href="#" class="btn-how">HOW IT WORKS<br>ON IT</a>
  </div>
</section>
<a href="#" class="btn-create">CREATE AN ACCOUNT</a>

<div class="welcome-mark">
  <span class="lead">Welcome to</span>
  <span class="name">Dinvora</span>
</div>
<p class="welcome-copy">Lorem Ipsum is simply dummy text of the printing and typesetting industry. Lorem Ipsum has been the industry's standard dummy text ever since the 1500s, when an unknown printer took a galley of type and scrambled it to make a type specimen book. It has survived not only five centuries, but also the leap into electronic typesetting, remaining essentially unchanged. It was popularised in the 1960s with the release of Letterfold sheets containing Lorem Ipsum passages, and more recently with desktop publishing software like Pagecraft Studio including versions of Lorem Ipsum.</p>

<section class="testimonial">
  <span class="quote-mark">&ldquo;</span>
  <blockquote>&ldquo;It has survived not only five centuries, but also the leap into electronic typesetting, remaining essentially unchanged. It was popularised in the 1960s with the release of Letterfold sheets containing Lorem Ipsum passages, and more recently with desktop publishing software like Pagecraft Studio including versions of Lorem Ipsum.&rdquo;</blockquote>
</section>
<div class="author-photo" role="img" aria-label="Portrait of the reviewer"></div>
<div class="author">
  <div class="author-name">Marlow Fenwick</div>
  <div class="author-role">Lorem Ipsim dolor</div>
</div>

<aside class="benefits">
  <svg width="233" height="510" viewBox="0 0 233 510">
    <path d="M0,0H233V488C170,470 80,505 0,485Z" fill="var(--orange-pale)"/>
    <path d="M0,0H233V392C170,370 80,408 0,385Z" fill="var(--orange-soft)"/>
    <path d="M0,0H233V297C170,275 80,313 0,290Z" fill="var(--orange-mid)"/>
    <path d="M0,0H233V200C170,178 80,216 0,195Z" fill="var(--orange-deep)"/>
    <path d="M0,0H233V82C170,100 80,75 0,97Z" fill="var(--ink)"/>
  </svg>
</aside>
<div class="benefits-badge"></div>
<h2 class="benefits-title">FOR YOUR BENEFITS</h2>

<div class="benefit" style="top:674px">
  <div class="benefit-icon">
    <svg width="34" height="34" viewBox="0 0 34 34" fill="none" stroke="#fff" stroke-width="2"><rect x="3" y="6" width="16" height="4"/><rect x="3" y="12" width="16" height="4"/><rect x="3" y="18" width="16" height="4"/><rect x="3" y="24" width="16" height="4"/><circle cx="24" cy="22" r="8" fill="#111"/><path d="M24 17v10M21.5 19.5h4a1.5 1.5 0 010 3h-3a1.5 1.5 0 000 3h4"/></svg>
  </div>
  <div class="benefit-label">EARN<br>EXTRA MONEY</div>
</div>
<div class="benefit" style="top:771px">
  <div class="benefit-icon">
    <svg width="34" height="34" viewBox="0 0 34 34" fill="none" stroke="#fff" stroke-width="2"><rect x="4" y="6" width="22" height="20" rx="2"/><path d="M4 12h22M10 3v6M20 3v6"/><circle cx="25" cy="25" r="6" fill="#111"/><path d="M25 22v3h2"/></svg>
  </div>
  <div class="benefit-label">FULLY MANAGE YOUR<br>BOOKINGS SCHEDULE</div>
</div>
<div class="benefit" style="top:868px">
  <div class="benefit-icon">
    <svg width="34" height="34" viewBox="0 0 34 34" fill="#fff"><path d="M3 8l14 4 14-4v18l-14 4-14-4z"/><path d="M13 13v10M21 13v10" stroke="#111" stroke-width="2"/></svg>
  </div>
  <div class="benefit-label">BE CREATIVE WITH<br>YOUR FOOD MENUS</div>
</div>
<div class="benefit" style="top:966px">
  <div class="benefit-icon">
    <svg width="34" height="34" viewBox="0 0 34 34" fill="none" stroke="#fff" stroke-width="2"><circle cx="17" cy="8" r="5"/><circle cx="7" cy="25" r="5"/><circle cx="27" cy="25" r="5"/><path d="M14 12l-5 8M20 12l5 8M12 25h10"/></svg>
  </div>
  <div class="benefit-label">EXPAND YOUR<br>CLIENT BASE</div>
</div>

<footer class="site-footer">
  <div class="social">
    <span>CHIRPWAVE</span>
    <span>CIRCLEPAGE</span>
    <span>VIDSTREAM</span>
    <span>ORBITPLUS</span>
    <span>WORKLINK</span>
  </div>
  <p class="copyright">© 2015 DINVORA. ALL RIGHTS RESERVED.</p>
</footer>

</body>
</html>
```